Business Card Design Project

2 sided business card utilizing existing logo
- English on one side, Arabic on the other side (both English and Arabic text will be provided)
Same color scheme as logo
Information included will be: name, title, email, phone, address and website (www.dravelnix.com)
Updates

Target Market(s)

We are a Systems Integration Company

Industry/Entity Type

Business

Font styles to use
Serif
Sans Serif

Requirements
Should not have
• We prefer using the flat logo rather than one with shadow/3D effect

```html
<!DOCTYPE html>
<html lang="en">
<head>
<meta charset="utf-8">
<title>Dravelnix Business Card</title>
<link rel="stylesheet" href="https://fonts.googleapis.com/css2?family=Open+Sans:wght@400;700&display=swap">
<style>
  :root {
    --brand-red: #ec2330;
    --paper: #ffffff;
    --ink: #4a4a4a;
    --backdrop: #e6e6e8;
  }
  * { margin: 0; padding: 0; box-sizing: border-box; }
  html, body { width: 1200px; height: 873px; overflow: hidden; }
  body {
    background: var(--backdrop);
    font-family: "Open Sans", Arial, sans-serif;
    position: relative;
  }
  .card {
    position: absolute;
    top: 286px;
    width: 520px;
    height: 300px;
    overflow: hidden;
    box-shadow: 0 6px 18px rgba(0,0,0,0.18);
  }
  .card--front { left: 60px; background: var(--paper); }
  .card--back { left: 620px; background: var(--brand-red); }

  .wordmark {
    position: absolute;
    display: flex;
    align-items: center;
    gap: 10px;
    font-weight: 700;
    letter-spacing: 5px;
    white-space: nowrap;
  }
  .wordmark__square { display: block; flex: none; }
  .card--front .wordmark { top: 40px; left: 250px; color: var(--brand-red); font-size: 20px; }
  .card--back .wordmark { top: 128px; left: 0; right: 0; justify-content: center; color: var(--paper); font-size: 30px; }

  .field-name {
    position: absolute; top: 26px; left: 26px;
    font-size: 13px; color: var(--ink);
  }
  .contact {
    position: absolute; top: 118px; left: 270px;
    list-style: none; font-size: 14px; line-height: 22px; color: var(--ink);
    white-space: nowrap;
  }
  .rule-thin {
    position: absolute; left: 0; right: 0; top: 214px; height: 9px;
    background: var(--brand-red);
  }
  .band {
    position: absolute; left: 0; right: 0; top: 232px; bottom: 0;
    background: var(--brand-red);
    display: flex; align-items: center; justify-content: center;
  }
  .band__url { color: var(--paper); font-size: 17px; letter-spacing: 3px; }
</style>
</head>
<body>
  <section class="card card--front" aria-label="Card front">
    <p class="field-name">NAME:</p>
    <div class="wordmark">
      <svg class="wordmark__square" width="16" height="16" viewBox="0 0 16 16"><rect width="16" height="16" fill="var(--brand-red)"/></svg>
      <span>DRAVELNIX</span>
    </div>
    <ul class="contact">
      <li>ADDRESS:&nbsp; northwave</li>
      <li>EMAIL:&nbsp; northwave</li>
      <li>PHONE: 1-98765-432</li>
    </ul>
    <div class="rule-thin"></div>
    <div class="band"><span class="band__url">www.dravelnix.com</span></div>
  </section>

  <section class="card card--back" aria-label="Card back">
    <div class="wordmark">
      <svg class="wordmark__square" width="22" height="22" viewBox="0 0 22 22"><rect width="22" height="22" fill="var(--paper)"/></svg>
      <span>DRAVELNIX</span>
    </div>
  </section>
</body>
</html>
```